Professional business cards for real estate development company

I need business cards for my new real estate development company. The company, "KORVA" is a real estate development, investment, and advisory firm with a focus on multifamily, office, and mixed-use projects across primary and secondary markets in the Southeast United States.

Style preference is modern

Industry/Entity Type

Real Estate Development

Contact Information for Business Card

The business cards need to include:
Name
Title
Mailing Address
Phone Number
Web Address

Logo is attached. I would like white to be the primary color with incorporation of the company colors: #232D3A and #B5A451

Font styles to use
Other font styles liked:
• Montserrat, Avenir

Requirements
Must have
• Company Logo. No need to include the company name since the name is in the logo.
Should not have
• No line type designs

```html
<!DOCTYPE html>
<html lang="en">
<head>
<meta charset="utf-8">
<title>KORVA Development – Business Cards</title>
<link rel="stylesheet" href="https://fonts.googleapis.com/css2?family=Montserrat:wght@400;500;700&display=swap">
<style>
  :root {
    --backdrop: #e4e4e4;
    --navy: #232d3a;
    --navy-top: #343f4e;
    --navy-bottom: #212a36;
    --gold: #b5a451;
    --paper: #ffffff;
    --muted: #e7eaee;
  }
  * { box-sizing: border-box; margin: 0; padding: 0; }
  html, body {
    width: 1200px; height: 1200px; overflow: hidden;
    background: var(--backdrop);
    font-family: "Montserrat", sans-serif;
  }
  .card {
    position: absolute;
    left: 262px;
    width: 685px;
    height: 391px;
    border-radius: 20px;
    overflow: hidden;
  }
  .card--front {
    top: 165px;
    background: var(--paper);
    display: flex; align-items: center; justify-content: center;
    padding-top: 70px;
  }
  .card--back { top: 653px; display: flex; }

  .wordmark {
    display: flex; flex-direction: column; align-items: center;
    font-weight: 500; line-height: 1;
    color: var(--navy);
  }
  .wordmark__row { display: flex; align-items: center; gap: 14px; }
  .wordmark__square { background: var(--gold); }
  .wordmark__name { letter-spacing: 2px; }
  .wordmark__sub { letter-spacing: 9px; }

  .card--front .wordmark__square { width: 20px; height: 20px; }
  .card--front .wordmark__name { font-size: 84px; }
  .card--front .wordmark__sub { font-size: 24px; margin-top: 14px; letter-spacing: 10px; }

  .back__brand {
    width: 350px; background: var(--paper);
    display: flex; align-items: center; justify-content: center;
    padding-top: 70px;
  }
  .back__brand .wordmark__square { width: 14px; height: 14px; }
  .back__brand .wordmark__name { font-size: 56px; }
  .back__brand .wordmark__sub { font-size: 17px; letter-spacing: 6px; margin-top: 10px; }

  .back__details {
    flex: 1;
    background: linear-gradient(180deg, var(--navy-top), var(--navy-bottom));
    color: var(--paper);
    padding: 98px 0 0 44px;
  }
  .person__name { font-size: 19px; font-weight: 700; letter-spacing: 0.5px; }
  .person__title { font-size: 14px; margin-top: 4px; color: var(--gold); font-weight: 500; }
  .address { font-size: 14px; line-height: 19px; margin-top: 19px; color: var(--muted); }
  .contacts { list-style: none; margin-top: 15px; }
  .contacts li {
    display: flex; align-items: center; gap: 9px;
    font-size: 14px; line-height: 19.5px; color: var(--muted);
  }
  .contacts svg { width: 12px; height: 12px; fill: var(--gold); flex: none; }
</style>
</head>
<body>
  <section class="card card--front" aria-label="Card front">
    <div class="wordmark">
      <div class="wordmark__row">
        <span class="wordmark__square"></span>
        <span class="wordmark__name">KORVA</span>
      </div>
      <span class="wordmark__sub">DEVELOPMENT</span>
    </div>
  </section>

  <section class="card card--back" aria-label="Card back">
    <div class="back__brand">
      <div class="wordmark">
        <div class="wordmark__row">
          <span class="wordmark__square"></span>
          <span class="wordmark__name">KORVA</span>
        </div>
        <span class="wordmark__sub">DEVELOPMENT</span>
      </div>
    </div>
    <div class="back__details">
      <p class="person__name">DANIEL REYES</p>
      <p class="person__title">President</p>
      <p class="address">2140 Alder Court<br>Savannah, Georgia 31401</p>
      <ul class="contacts">
        <li>
          <svg viewBox="0 0 24 24"><path d="M6.6 10.8c1.4 2.8 3.8 5.1 6.6 6.6l2.2-2.2c.3-.3.7-.4 1-.2 1.1.4 2.3.6 3.6.6.6 0 1 .4 1 1V20c0 .6-.4 1-1 1C10.6 21 3 13.4 3 4c0-.6.4-1 1-1h3.5c.6 0 1 .4 1 1 0 1.3.2 2.5.6 3.6.1.3 0 .7-.2 1z"/></svg>
          555-214-7730
        </li>
        <li>
          <svg viewBox="0 0 24 24"><path d="M7 1h10c1.1 0 2 .9 2 2v18c0 1.1-.9 2-2 2H7c-1.1 0-2-.9-2-2V3c0-1.1.9-2 2-2zm0 3v15h10V4z"/></svg>
          555-318-4062
        </li>
        <li>
          <svg viewBox="0 0 24 24"><path d="M2 5h20v14H2zm2 2v.5l8 5 8-5V7z"/></svg>
          info@korvadevelopment.com
        </li>
        <li>
          <svg viewBox="0 0 24 24"><path d="M12 2a10 10 0 1 0 0 20 10 10 0 0 0 0-20zm-1 17.9A8 8 0 0 1 4.2 10.2L9 15v1c0 1.1.9 2 2 2zm6.9-2.5c-.3-.8-1-1.4-1.9-1.4h-1v-3c0-.6-.4-1-1-1H8v-2h2c.6 0 1-.4 1-1V7h2c1.1 0 2-.9 2-2v-.4a8 8 0 0 1 2.9 12.8z"/></svg>
          www.korvadevelopment.com
        </li>
      </ul>
    </div>
  </section>
</body>
</html>
```